Meadowlark Learning Growth Partners (MLGP)

This is a professional business card. Logo and picture are a must on the front of the card. I am an educational consultant. I have been consulting for the past three years for a company. I am now opening my own company. My goal for my consulting company is to eventually consult all over America.

Target Market(s)

Educators, schools, professionals

Industry/Entity Type

Consulting

Contact Information for Business Card

Picture/logo on front, simple modern design

Font styles to use
Serif

Colors
85abd2
0355a3
3176b5
cedeed

Requirements
Must have
• picture, logo,
• Odessa Pruitt, Ed.S
• address 5073 Cormorant ridge Dr. Nashville, TN 37940
• Cell:616-555-0148
• Office: 629-555-0172
• www.Mlgpedu.example
• pruittodessa@mailbox.example

```html
<!DOCTYPE html>
<html lang="en">
<head>
<meta charset="utf-8">
<title>MLGP Business Card</title>
<link rel="stylesheet" href="https://fonts.googleapis.com/css2?family=Open+Sans:wght@400;600;700;800&display=swap">
<style>
  :root {
    --page-bg: #e4e7ec;
    --card-white: #ffffff;
    --brand-navy: #123f86;
    --brand-blue: #1257a6;
    --band-dark: #053a78;
    --name-blue: #1f5fae;
    --text-grey: #5a5a5a;
    --rule-light: #e8eef6;
  }
  * { margin: 0; padding: 0; box-sizing: border-box; }
  html, body { width: 1200px; height: 1000px; overflow: hidden; }
  body {
    background: var(--page-bg);
    font-family: "Open Sans", Arial, sans-serif;
    position: relative;
  }
  .card {
    position: absolute;
    left: 276px;
    width: 642px;
    height: 366px;
    background: var(--card-white);
    border-radius: 40px;
    overflow: hidden;
  }
  .card-front { top: 84px; }
  .card-back { top: 537px; }

  /* Front */
  .front-mark {
    position: absolute;
    left: 50%;
    top: 92px;
    width: 84px;
    height: 84px;
    margin-left: -42px;
    border-radius: 50%;
    background: var(--brand-navy);
  }
  .front-wordmark {
    position: absolute;
    left: 0; right: 0;
    top: 222px;
    text-align: center;
    font-weight: 800;
    font-size: 62px;
    line-height: 1;
    letter-spacing: 3px;
    color: var(--brand-navy);
  }

  /* Back */
  .brand-lockup { position: absolute; left: 36px; top: 26px; display: flex; align-items: center; }
  .brand-dot { width: 34px; height: 34px; border-radius: 50%; background: var(--brand-navy); }
  .brand-initials {
    margin-left: 12px;
    font-weight: 800;
    font-size: 22px;
    letter-spacing: 1.5px;
    color: var(--brand-navy);
  }
  .brand-divider { width: 1.5px; height: 56px; background: var(--brand-navy); margin: 0 8px 0 10px; }
  .brand-fullname {
    font-weight: 700;
    font-size: 11px;
    line-height: 15px;
    color: var(--brand-navy);
  }
  .person-name {
    position: absolute; left: 34px; top: 97px;
    font-size: 27px; font-weight: 400; color: var(--name-blue);
  }
  .person-credential {
    position: absolute; left: 35px; top: 137px;
    font-size: 18px; color: var(--text-grey);
  }
  .contact-band {
    position: absolute; left: 0; top: 169px;
    width: 100%; height: 137px;
    background: var(--brand-blue);
  }
  .address {
    position: absolute; left: 36px; top: 179px;
    font-size: 16px; color: #fff;
  }
  .contact-list { position: absolute; left: 34px; top: 212px; list-style: none; }
  .contact-list li {
    display: flex; align-items: center;
    height: 30px;
    font-size: 18px; color: #fff;
  }
  .contact-list svg { width: 18px; height: 18px; margin-right: 14px; flex: none; }
  .band-rule { position: absolute; left: 0; top: 306px; width: 100%; height: 3px; background: var(--rule-light); }
  .website-band {
    position: absolute; left: 0; top: 309px;
    width: 100%; height: 57px;
    background: var(--band-dark);
  }
  .website {
    position: absolute; right: 244px; top: 321px;
    font-size: 18px; color: #fff;
  }
  .portrait {
    position: absolute; left: 404px; top: 46px;
    width: 238px; height: 320px;
    background: linear-gradient(180deg, #d9c79a 0%, #e7cdbb 32%, #f2f2f2 52%, #1d2028 70%, #16181f 100%);
  }
</style>
</head>
<body>
  <section class="card card-front">
    <div class="front-mark"></div>
    <div class="front-wordmark">MLGP</div>
  </section>

  <section class="card card-back">
    <div class="brand-lockup">
      <div class="brand-dot"></div>
      <div class="brand-initials">MLGP</div>
      <div class="brand-divider"></div>
      <div class="brand-fullname">Meadowlark<br>Learning<br>Growth<br>Partners</div>
    </div>

    <div class="person-name">Odessa Pruitt</div>
    <div class="person-credential">Ed.S</div>

    <div class="contact-band"></div>
    <div class="address">5073 Cormorant ridge Dr. Nashville, TN 37940</div>
    <ul class="contact-list">
      <li>
        <svg viewBox="0 0 20 20" aria-hidden="true"><circle cx="10" cy="10" r="8.5" fill="none" stroke="#fff" stroke-width="1.6"/><path d="M7 5.5l1.6 2.4-1 1.1c.6 1.3 1.5 2.2 2.8 2.8l1.1-1 2.4 1.6-.9 1.6c-3.4-.3-6.2-3.1-6.5-6.5z" fill="#fff"/></svg>
        616-555-0148
      </li>
      <li>
        <svg viewBox="0 0 20 20" aria-hidden="true"><path d="M2 7c0-2 3.5-3 8-3s8 1 8 3v1.5h-4V7H6v1.5H2z" fill="#fff"/><path d="M5 9h10l2 7H3z" fill="#fff"/><circle cx="10" cy="12.5" r="2" fill="#1257a6"/></svg>
        629-555-0172
      </li>
      <li>
        <svg viewBox="0 0 20 20" aria-hidden="true"><rect x="2" y="5" width="16" height="11" fill="#fff"/><path d="M2.5 5.5L10 11l7.5-5.5" fill="none" stroke="#1257a6" stroke-width="1.4"/></svg>
        pruittodessa@mailbox.example
      </li>
    </ul>

    <div class="band-rule"></div>
    <div class="website-band"></div>
    <div class="website">www.Mlgpedu.example</div>

    <div class="portrait" role="img" aria-label="Portrait photo of Odessa Pruitt in a dark blazer and white blouse"></div>
  </section>
</body>
</html>
```